Film Poster Design For Japanese Film Poster #2

The title of this colour film is KAZE YAMA TSUKI HOSHI春 夏 秋 冬Translated this is literallySpring Summer Fall Winter ... however the English title is FOUR SEASONSWe attached a series of screen shots from the film and also the computer generated Kanji characters. We will be updating the brief with the Japanese title characters which currently being hand painted.We require the post in two formats. One being the traditional poster format and the other being in a wide screen ration of 1000px by 465px. Same design.This is a drama, feature length film comprising of four separate stories. The is mixture of Japanese and English dialogue. We are looking at 2 possible designs. You can choose to submit either.1: A with lots of white space ... focussing on smaller images at the Japanese text. I have uploaded a sample poster as a very rough indication. "Stories nobody ever wrote down about the quiet ones" / "Odile Bettina Rue Ingrid" - Lots of white space.Ideally we would have liked to have had the image of the young girl in the kimono pulling on the bell rope clear cut and used on white as a single main image. However, we are not sure that the clarity or resolution of the original image is sufficient. 2: One with lots of images as you can see with the two "Bridge Of Dust" Sample posters.Obviously we are not looking for a copy of either poster, but these posters are a guide to the two looks we are after.Thanks. Kaede
Hello all,Apologies for the delay. We have had to work through some naming issues.The film's English title has had to be renamed to THE LANTERNS. Please do not used TEN LANTERNS in any designed moving forward.Thanks Kaede Added Sunday, May 25, 2014

```html
<!DOCTYPE html>
<html lang="en">
<head>
<meta charset="utf-8">
<title>Kaze Yama Tsuki Hoshi — Film Poster</title>
<link rel="stylesheet" href="https://fonts.googleapis.com/css2?family=Bebas+Neue&family=Noto+Sans+JP:wght@700&family=Oswald:wght@600&display=swap">
<style>
  :root {
    --bg-light: #d2d2d2;
    --bg-mid: #b4b4b4;
    --bg-dark: #5c5c5c;
    --ink: #181417;
    --still-deep: #1c1220;
    --still-plum: #4e2450;
    --still-rose: #b2457f;
    --still-violet: #6a3a8c;
  }
  * { margin: 0; padding: 0; box-sizing: border-box; }
  html, body {
    width: 1200px;
    height: 558px;
    overflow: hidden;
  }
  body {
    background: linear-gradient(100deg, var(--bg-light) 0%, var(--bg-mid) 45%, #8c8c8c 75%, var(--bg-dark) 100%);
    color: var(--ink);
    position: relative;
  }
  .poster {
    position: relative;
    width: 1200px;
    height: 558px;
  }
  .kanji-title {
    position: absolute;
    top: 138px;
    left: 150px;
    display: flex;
    font-family: "Noto Sans JP", sans-serif;
    font-weight: 700;
    font-size: 184px;
    line-height: 1;
  }
  .kanji-title__char {
    width: 254px;
    display: block;
    background: linear-gradient(135deg, var(--still-deep) 0%, var(--still-rose) 28%, var(--still-plum) 48%, var(--still-violet) 62%, var(--still-rose) 78%, var(--still-deep) 100%);
    -webkit-background-clip: text;
    background-clip: text;
    color: transparent;
  }
  .romaji-title {
    position: absolute;
    top: 322px;
    left: 0;
    width: 1200px;
    text-align: center;
    font-family: "Bebas Neue", sans-serif;
    font-size: 108px;
    line-height: 1;
    letter-spacing: 5px;
    word-spacing: 10px;
    color: var(--ink);
  }
  .credits {
    position: absolute;
    top: 492px;
    left: 418px;
    width: 340px;
    color: var(--ink);
  }
  .credits__roles {
    font-family: "Oswald", sans-serif;
    font-weight: 600;
    font-size: 16px;
    line-height: 18px;
    text-align: center;
    letter-spacing: 0.5px;
  }
  .credits__block {
    margin-top: 3px;
    font-family: "Oswald", sans-serif;
    font-weight: 600;
    font-size: 6.6px;
    line-height: 9px;
    text-align: justify;
    text-align-last: justify;
    text-transform: uppercase;
  }
</style>
</head>
<body>
  <main class="poster">
    <h1 class="kanji-title" role="img" aria-label="Title kanji 風 山 月 星 filled with a purple and pink film still">
      <span class="kanji-title__char">風</span>
      <span class="kanji-title__char">山</span>
      <span class="kanji-title__char">月</span>
      <span class="kanji-title__char">星</span>
    </h1>
    <p class="romaji-title">KAZE YAMA TSUKI HOSHI</p>
    <section class="credits">
      <p class="credits__roles">REALISATOR - PRODUCER - EXECUTIVE PROD</p>
      <p class="credits__block">Praesent et est nisi. Aenean viverra in sem ac suscipit. Nulla facilisi. Duis condimentum leo id ante convallis fermentum eu quis dui. Suspendisse condimentum quam nisi, eu adipiscing lorem interdum ut. Morbi interdum, enim vitae lobortis consequat, metus nibh elementum purus, eu ullamcorper augue est a massa. Curabitur</p>
    </section>
  </main>
</body>
</html>
```